Luxury Wine Label for New Startup Winery

We need a wine label for our new winery startup. We have worked with a local designer but do not feel the resulting label / logo have the elevation required to present our brand as a luxury wine. Our winery is called "Harrowgate Vineyards" and we are focused on extremely high quality hand crafted artisan and estate wines from the Pacific Northwest.
We would like to see designs that utilize a tree line, or other imagery that represents the "Harrowgate" part of our company name. Another interesting feature could be wood grain.
A logo will be required based on your design so please design with this in mind:
This logo should be consistent with the wine bottle label design, and should be representative of our high end exclusive wine while giving a sense of place (Oregon/ Pacific Northwest.)
I will supply an image of the design we received from our local designer, PLEASE NOTE: in general we do like wood grain and tree line concepts but feel the execution was poorly done.
ATTN: Logo design should be suitable for use on: Bottles (Red wine/rose/white wine), Bussiness cards, vehicle signage, business signage, etc
P.S.:
If you have a design that is not outside the box we are still interested in seeing it.
Label is for a burgundy style bottle with a label height of 3.5 - 4" and a width of 3.5-4"
any label <= 4"x4" and >=3.5"x3.5" will be acceptable:
HOWEVER Width should be greater than or equal to height due to the bottle format
Target Market(s)
Wine enthusiasts with adequate discretionary budgets to afford $100 bottles of wine.
Industry/Entity Type
Wine / Winery
Requirements
Must have
- A sense of luxury, a feel of exclusivity, and a theme consistent with our product and brand name
Nice to have
- Tree line, wood grain or other wood themes. Serif fonts
Should not have
- anything cheesy, off topic, hard to read script fonts or anything that makes the label hard to read from a few feet away or too busy

```html
<!DOCTYPE html>
<html lang="en">
<head>
<meta charset="utf-8">
<title>Harrowgate Vineyards – Label Presentation</title>
<link rel="stylesheet" href="https://fonts.googleapis.com/css2?family=Libre+Baskerville:wght@400;700&display=swap">
<style>
  :root {
    --canvas: #ffffff;
    --burgundy: #4e2230;
    --burgundy-deep: #3a1720;
    --burgundy-light: #5e2a3a;
    --gold: #e8c14a;
    --gold-rim: #d9a93a;
    --gold-soft: #c99a3a;
    --cream: #e9e3d0;
    --ornament: #6b4020;
    --ornament-deep: #4a2a12;
    --rose-box: #b21fb8;
    --white-box: #c8321b;
    --ink: #2b1418;
    --black: #000000;
    --paper: #ffffff;
    --studio: #ecebe8;
    --studio-edge: #cfcfcc;
    --glass: #2a1a1c;
  }
  * { margin: 0; padding: 0; box-sizing: border-box; }
  html, body { width: 843px; height: 1200px; overflow: hidden; background: var(--canvas); }
  .sheet { position: relative; width: 843px; height: 1200px; }

  .label {
    position: absolute; left: 0; width: 442px; height: 388px;
    overflow: hidden; background: var(--burgundy);
  }
  .label--syrah { top: 0; }
  .label--rose { top: 401px; }
  .label--white { top: 812px; }

  .label__rim {
    position: absolute; left: 0; right: 0; top: 0; height: 11px;
    background: linear-gradient(180deg, var(--gold-rim), var(--gold-soft));
  }
  .label__grain {
    position: absolute; left: 0; right: 0; top: 11px; height: 268px;
    background:
      radial-gradient(ellipse 120px 60px at 22% 30%, var(--burgundy-light), transparent 70%),
      radial-gradient(ellipse 140px 70px at 80% 68%, var(--burgundy-light), transparent 70%),
      radial-gradient(ellipse 100px 50px at 60% 15%, var(--burgundy-deep), transparent 70%),
      linear-gradient(100deg, var(--burgundy-deep), var(--burgundy) 40%, var(--burgundy-light) 60%, var(--burgundy-deep));
  }
  .label__mark {
    position: absolute; left: 187px; top: 48px; width: 68px; height: 68px;
    background: var(--gold);
  }
  .label__name {
    position: absolute; left: 0; right: 0; top: 170px;
    text-align: center; color: var(--gold);
    font-family: "Libre Baskerville", serif; font-weight: 700; line-height: 1;
  }
  .label__name-main { display: block; font-size: 38px; letter-spacing: 1px; }
  .label__name-sub { display: block; font-size: 26px; margin-top: 2px; padding-left: 150px; }

  .label__region {
    position: absolute; left: 0; right: 0; top: 279px; height: 59px;
    background: var(--cream); color: var(--ink);
    font-family: "Libre Baskerville", serif; text-align: center; line-height: 1;
  }
  .label__valley { display: block; font-size: 16px; margin-top: 10px; letter-spacing: 0.5px; }
  .label__year { display: block; font-size: 13px; margin-top: 8px; letter-spacing: 1px; }

  .label__ornament {
    position: absolute; left: 0; right: 0; top: 338px; height: 46px;
    border-top: 3px solid var(--gold-rim);
    border-bottom: 3px solid var(--gold-rim);
    background:
      linear-gradient(180deg, transparent 30%, rgba(217,169,58,0.35) 50%, transparent 70%),
      linear-gradient(90deg, var(--ornament-deep), var(--ornament) 25%, var(--ornament-deep) 50%, var(--ornament) 75%, var(--ornament-deep));
  }
  .label__varietal {
    position: absolute; left: 126px; width: 188px; top: 338px; height: 44px;
    color: var(--gold); font-family: "Libre Baskerville", serif;
    font-size: 30px; text-align: center; line-height: 46px; letter-spacing: 1px;
  }
  .label--syrah .label__varietal { background: var(--burgundy-deep); }
  .label--rose .label__varietal { background: var(--rose-box); }
  .label--white .label__varietal { background: var(--white-box); }

  .wordmark {
    position: absolute; left: 482px; top: 110px; width: 323px; height: 131px;
    background: var(--black); color: var(--paper);
    font-family: "Libre Baskerville", serif; font-weight: 700;
    text-align: center; line-height: 1;
  }
  .wordmark__main { display: block; font-size: 32px; margin-top: 30px; letter-spacing: 1px; }
  .wordmark__sub { display: block; font-size: 24px; margin-top: 2px; padding-left: 120px; }

  .brand-tile {
    position: absolute; left: 552px; top: 317px; width: 201px; height: 206px;
    background: var(--black); color: var(--paper);
    font-family: "Libre Baskerville", serif; font-weight: 700;
    display: flex; align-items: center; justify-content: center;
    font-size: 19px; letter-spacing: 0.5px;
  }

  .bottle-scene {
    position: absolute; left: 447px; top: 605px; width: 396px; height: 595px;
    background:
      radial-gradient(ellipse 22px 40px at 50% 17%, #a8915a, transparent 100%),
      radial-gradient(ellipse 44px 130px at 50% 52%, var(--burgundy), transparent 100%),
      radial-gradient(ellipse 48px 200px at 50% 60%, var(--glass) 60%, transparent 100%),
      radial-gradient(ellipse at 50% 45%, var(--studio), var(--studio-edge));
  }
</style>
</head>
<body>
<main class="sheet">

  <section class="label label--syrah">
    <div class="label__rim"></div>
    <div class="label__grain" role="img" aria-label="Burgundy wood grain texture"></div>
    <div class="label__mark"></div>
    <h2 class="label__name"><span class="label__name-main">HARROWGATE</span><span class="label__name-sub">Vineyard</span></h2>
    <div class="label__region"><span class="label__valley">WILLAMETTE VALLEY</span><span class="label__year">-2024-</span></div>
    <div class="label__ornament" role="img" aria-label="Gold ornamental border band"></div>
    <div class="label__varietal">SYRAH</div>
  </section>

  <section class="label label--rose">
    <div class="label__rim"></div>
    <div class="label__grain" role="img" aria-label="Burgundy wood grain texture"></div>
    <div class="label__mark"></div>
    <h2 class="label__name"><span class="label__name-main">HARROWGATE</span><span class="label__name-sub">Vineyard</span></h2>
    <div class="label__region"><span class="label__valley">WILLAMETTE VALLEY</span><span class="label__year">-2024-</span></div>
    <div class="label__ornament" role="img" aria-label="Gold ornamental border band"></div>
    <div class="label__varietal">ROSE</div>
  </section>

  <section class="label label--white">
    <div class="label__rim"></div>
    <div class="label__grain" role="img" aria-label="Burgundy wood grain texture"></div>
    <div class="label__mark"></div>
    <h2 class="label__name"><span class="label__name-main">HARROWGATE</span><span class="label__name-sub">Vineyard</span></h2>
    <div class="label__region"><span class="label__valley">WILLAMETTE VALLEY</span><span class="label__year">-2024-</span></div>
    <div class="label__ornament" role="img" aria-label="Gold ornamental border band"></div>
    <div class="label__varietal">WHITE</div>
  </section>

  <div class="wordmark"><span class="wordmark__main">HARROWGATE</span><span class="wordmark__sub">Vineyard</span></div>

  <div class="brand-tile">HARROWGATE</div>

  <div class="bottle-scene" role="img" aria-label="Photograph of a dark wine bottle with gold foil neck wearing the Syrah label"></div>

</main>
</body>
</html>
```